KRV Business Cards

We are a local commercial development company based in Silicon Valley and we would like a new business card. I've attached a copy of our company brochure to give a flavor of what we do, our logo, info company colors/graphics, and our current business card. We don't necessarily need a crazy makeover, but would like something that feels a little bit more "fresh" and modern (we've had the same business card design for 15+ years), but still in keeping with our overall brand -- clean, high-quality, modern but timeless. Would like to add our website to the info on the card (www.velmara.com) and would like the flexibility for some folks to have an efax number listed and some not to have that included (without it looking like there is a hole).

```html
<!DOCTYPE html>
<html lang="en">
<head>
<meta charset="utf-8">
<title>Velmara Development Company – Business Card</title>
<link rel="stylesheet" href="https://fonts.googleapis.com/css2?family=EB+Garamond:wght@400;500&family=Tinos&display=swap">
<style>
  :root {
    --slate: #2f3c3b;
    --teal-dark: #33534f;
    --teal-mid: #7f9a98;
    --teal-light: #c9d4d3;
    --navy: #1b2a5c;
    --signal-red: #ec1c16;
    --paper: #f8f8f8;
  }
  html, body {
    margin: 0;
    padding: 0;
    overflow: hidden;
    background: #ffffff;
  }
  .card {
    position: relative;
    width: 1200px;
    height: 720px;
    overflow: hidden;
    background: var(--paper);
    font-family: "Tinos", "Times New Roman", serif;
  }
  .texture-band {
    position: absolute;
    left: 0;
    top: 0;
    width: 1200px;
    height: 416px;
    background:
      linear-gradient(90deg, var(--teal-mid) 0%, var(--teal-light) 30%, var(--teal-mid) 55%, var(--teal-light) 75%, var(--teal-mid) 100%);
  }
  .company-name {
    position: absolute;
    left: 94px;
    top: 62px;
    margin: 0;
    font-family: "EB Garamond", "Times New Roman", serif;
    font-weight: 400;
    font-size: 62px;
    line-height: 74px;
    letter-spacing: 1px;
    color: var(--slate);
    text-transform: uppercase;
  }
  .accent-bar {
    position: absolute;
    left: 228px;
    top: 402px;
  }
  .person {
    position: absolute;
    right: 0;
    top: 420px;
    width: 600px;
    text-align: right;
    font-family: "EB Garamond", "Times New Roman", serif;
    color: var(--teal-dark);
  }
  .person-name {
    margin: 0;
    font-size: 62px;
    line-height: 66px;
    font-weight: 400;
    letter-spacing: 1px;
  }
  .person-title {
    margin: 0;
    padding-right: 142px;
    font-size: 56px;
    line-height: 50px;
    font-weight: 400;
  }
  .contact-list {
    position: absolute;
    left: 78px;
    top: 460px;
    margin: 0;
    padding: 0;
    list-style: none;
    color: var(--navy);
    font-size: 28px;
  }
  .contact-item {
    display: flex;
    align-items: center;
    height: 30px;
    margin-bottom: 15px;
  }
  .contact-item.address { margin-top: 6px; margin-bottom: 22px; }
  .contact-item .icon {
    width: 28px;
    height: 28px;
    margin-right: 18px;
    fill: var(--signal-red);
  }
  .contact-item.address .icon { margin-right: 4px; width: 24px; }
  .contact-item .web-icon { margin-left: 28px; margin-right: 10px; }
</style>
</head>
<body>
<div class="card">
  <div class="texture-band" role="img" aria-label="Textured teal-grey stone surface with vertical streaks"></div>

  <h1 class="company-name">Velmara<br>Development<br>Company,LLC</h1>

  <svg class="accent-bar" width="745" height="18" viewBox="0 0 745 18" aria-hidden="true">
    <path d="M14 0 H745 L733 16 H0 Q2 2 14 0 Z" fill="var(--signal-red)"/>
  </svg>

  <div class="person">
    <p class="person-name">CORIN A . HALVEY</p>
    <p class="person-title">Partner</p>
  </div>

  <ul class="contact-list">
    <li class="contact-item">
      <svg class="icon" viewBox="0 0 24 24" aria-hidden="true"><path d="M6.6 10.8a15 15 0 0 0 6.6 6.6l2.2-2.2a1 1 0 0 1 1-.25 11.4 11.4 0 0 0 3.6.57 1 1 0 0 1 1 1V20a1 1 0 0 1-1 1A17 17 0 0 1 3 4a1 1 0 0 1 1-1h3.5a1 1 0 0 1 1 1c0 1.25.2 2.45.57 3.6a1 1 0 0 1-.25 1z"/><path d="M14 2.5a7.5 7.5 0 0 1 7.5 7.5h-1.8A5.7 5.7 0 0 0 14 4.3zM14 6a4 4 0 0 1 4 4h-1.8A2.2 2.2 0 0 0 14 7.8z"/></svg>
      <span>650.555.0138</span>
    </li>
    <li class="contact-item">
      <svg class="icon" viewBox="0 0 24 24" aria-hidden="true"><path d="M6.6 10.8a15 15 0 0 0 6.6 6.6l2.2-2.2a1 1 0 0 1 1-.25 11.4 11.4 0 0 0 3.6.57 1 1 0 0 1 1 1V20a1 1 0 0 1-1 1A17 17 0 0 1 3 4a1 1 0 0 1 1-1h3.5a1 1 0 0 1 1 1c0 1.25.2 2.45.57 3.6a1 1 0 0 1-.25 1z"/><path d="M14 2.5a7.5 7.5 0 0 1 7.5 7.5h-1.8A5.7 5.7 0 0 0 14 4.3zM14 6a4 4 0 0 1 4 4h-1.8A2.2 2.2 0 0 0 14 7.8z"/></svg>
      <span>650.555.0177</span>
    </li>
    <li class="contact-item">
      <svg class="icon" viewBox="0 0 24 24" aria-hidden="true"><path d="M1 5h22v14H1z M2.5 6.2 12 13l9.5-6.8V6.2z" fill-rule="evenodd"/></svg>
      <span>corin@velmara.com</span>
    </li>
    <li class="contact-item address">
      <svg class="icon" viewBox="0 0 24 24" aria-hidden="true"><path d="M12 1a8 8 0 0 0-8 8c0 6 8 14 8 14s8-8 8-14a8 8 0 0 0-8-8zm0 11a3 3 0 1 1 0-6 3 3 0 0 1 0 6z"/></svg>
      <span>412 Marren Avenue,Palo Alto,California 94301</span>
    </li>
    <li class="contact-item">
      <svg class="icon" viewBox="0 0 24 24" aria-hidden="true" style="width:36px;height:40px;margin-right:14px"><path d="M6 1h12v6H6z M2 8h20v10h-4v-3H6v3H2z M7 16h10v7H7z M9 18h6v1H9z M9 20.5h6v1H9z" fill-rule="evenodd"/></svg>
      <span>650.555.0191</span>
      <svg class="icon web-icon" viewBox="0 0 24 24" aria-hidden="true"><path d="M12 1a11 11 0 1 0 0 22 11 11 0 0 0 0-22zm0 2c1.4 1.6 2.3 3.7 2.6 6H9.4C9.7 6.7 10.6 4.6 12 3zM9.4 11h5.2c-.1 2.4-1 4.6-2.6 6.6-1.6-2-2.5-4.2-2.6-6.6zM3.1 11h4.3c.1 2.3.8 4.5 2 6.4A9 9 0 0 1 3.1 11zm0-2a9 9 0 0 1 6.3-6.4C8.2 4.4 7.5 6.6 7.4 9zm13.5 2h4.3a9 9 0 0 1-6.3 6.4c1.2-1.9 1.9-4.1 2-6.4zm0-2c-.1-2.4-.8-4.6-2-6.4A9 9 0 0 1 20.9 9z M11 19h2v2h-2z"/></svg>
      <span>www.velmara.com</span>
    </li>
  </ul>
</div>
</body>
</html>
```